Varnock Travel letterhead design

We need a design for a simple document where we can dump our own information within it. A simple letterhead style. No address or phone details etc are required. More just our logo and free format. Hope this makes sense !

```html
<!DOCTYPE html>
<html lang="en">
<head>
<meta charset="utf-8">
<title>Varnock Travel Letterhead</title>
<link rel="stylesheet" href="https://fonts.googleapis.com/css2?family=Arimo:wght@400&display=swap">
<style>
  :root {
    --backdrop: #e4e2dd;
    --paper: #fffef5;
    --ink-blue: #48658d;
    --tagline-grey: #a9aaa6;
  }
  * { box-sizing: border-box; margin: 0; padding: 0; }
  html, body {
    width: 1200px;
    height: 900px;
    overflow: hidden;
    background: var(--backdrop);
    font-family: "Arimo", Arial, sans-serif;
  }
  .letterhead {
    position: absolute;
    left: 275px;
    top: 30px;
    width: 650px;
    height: 840px;
    background: var(--paper);
    box-shadow: 0 2px 10px rgba(0, 0, 0, 0.12);
  }
  .brand {
    position: absolute;
    left: 54px;
    top: 74px;
  }
  .brand-name {
    font-weight: 400;
    font-size: 28px;
    line-height: 1;
    letter-spacing: 1px;
    color: var(--ink-blue);
  }
  .brand-tagline {
    margin-top: 5px;
    font-weight: 400;
    font-size: 12px;
    letter-spacing: 0.6px;
    color: var(--tagline-grey);
  }
  .footer-band {
    position: absolute;
    left: 0;
    bottom: 0;
    width: 100%;
    height: 10px;
    background: var(--ink-blue);
  }
</style>
</head>
<body>
  <main class="letterhead">
    <header class="brand">
      <div class="brand-name">Varnock</div>
      <div class="brand-tagline">TRAVEL CORPORATION</div>
    </header>
    <div class="footer-band"></div>
  </main>
</body>
</html>
```